Website for a health information tech company

I need a website for a new startup company, VelaTrove, Inc. that specializes in healthcare information technology. VelaTrove is a monitoring system that uses wearable sensors and predictive algorithms to detect when an elderly persons health is declining and triggers progressively higher levels of interventions.

The site needs to be very simple, elegant and initially will have minimal information as company and product is still under development and is in a stealth mode. I like the lumbrofield.com website as it has a "single page" look and feel with sliding vertical sections. Ideally the sections would be "Home", "Technology", "Customers", "News", "About Us" and "Contact Us". The contact us should have a contact form that gets sent to an email address.

I have a couple of example sites that my site should take inspiration from (lumbrofield.com and nodwickpath.com). I would like a WordPress backend so I can easily update content so the winning design should be easily importable or setup into Wordpress.

Target Market(s)

Investors, Customers (Doctors, Patients, Health Insurance companies, Hospital directors)

Industry/Entity Type

Healthcare

Requirements
Must have
• top horizontal menu that gets repeated on each vertical slide. Should have animated vertical slides. Must be viewable on any device (iPad, Android Tablets) correctly and must render correctly on different screen sizes. Must be viewable in all popular browsers. Must work well with touchscreen devices such as iPad, iPhone, Android tablets and phones.
Must have a content management system backend such as WordPress so I can edit/update content and in future add additional sections, images etc.

See attached company logo so colors must be complimentary to the logo colors. Feel free to use the logo colors as web site theme colors if it makes sense.
Nice to have
• Nice subtle textured background like linen or leather.
Should not have
• Not looking for traditional web site design with nav bars on left etc
Should not feel like a traditional web site where you click a link and another page loads. It must be animated slide into a different section. No flash or any other technology that requires plug ins.

```html
<!DOCTYPE html>
<html lang="en">
<head>
<meta charset="utf-8">
<title>VelaTrove – Our Technology</title>
<link rel="stylesheet" href="https://fonts.googleapis.com/css2?family=Fjalla+One&family=Ubuntu:ital,wght@0,400;0,500;0,700;1,700&display=swap">
<style>
  :root {
    --bg: #ebe7f1;
    --bg-line: rgba(210, 195, 220, 0.35);
    --accent: #f7941d;
    --heading: #2a2a2a;
    --text: #262626;
    --card: #f4e5c6;
    --card-head: #f7ebd0;
    --card-border: #e7d3a8;
    --tick: #8cc63f;
    --tick-dark: #5e9b1e;
  }
  * { box-sizing: border-box; margin: 0; padding: 0; }
  html, body { width: 1200px; height: 1033px; overflow: hidden; }
  body {
    background-color: var(--bg);
    background-image:
      repeating-linear-gradient(35deg, var(--bg-line) 0 1px, transparent 1px 9px),
      repeating-linear-gradient(-35deg, var(--bg-line) 0 1px, transparent 1px 11px);
    font-family: "Ubuntu", sans-serif;
    color: var(--text);
    position: relative;
  }
  .section-title {
    position: absolute; left: 73px; top: 46px;
    font-family: "Fjalla One", sans-serif; font-weight: 400;
    font-size: 31px; line-height: 40px; color: var(--accent);
    letter-spacing: 0.3px; text-transform: uppercase;
  }
  .feature-cards { position: absolute; left: 74px; top: 112px; width: 1050px; height: 270px; }
  .feature-card {
    position: absolute; top: 0; width: 249px; height: 263px;
    background: var(--card);
    border: 1px solid var(--card-border);
    box-shadow: 0 8px 10px -6px rgba(0,0,0,0.3);
  }
  .feature-card:nth-child(1) { left: 0; }
  .feature-card:nth-child(2) { left: 266px; }
  .feature-card:nth-child(3) { left: 531px; }
  .feature-card:nth-child(4) { left: 803px; }
  .card-title {
    height: 52px; line-height: 52px; text-align: center;
    background: var(--card-head);
    border-bottom: 1px solid var(--card-border);
    font-weight: 500; font-size: 17px; color: var(--heading);
    text-transform: uppercase; white-space: nowrap;
  }
  .card-media {
    margin: 17px 13px 0; height: 100px;
    border: 1px solid #d9cbb0;
  }
  .media-care { background: linear-gradient(90deg, #c9ccd0, #e8dcd2 60%, #d9b9a0); }
  .media-assess { background: linear-gradient(120deg, #e9eef3, #c7d3de 55%, #22324a); }
  .media-gears { background: radial-gradient(circle at 50% 50%, #8cc63f 0 30%, #ffffff 32%); }
  .media-clinic { background: linear-gradient(90deg, #f1f1f1, #e8d3c3 50%, #f3f3f3 75%, #111 80%); }
  .card-text { margin: 12px 13px 0; font-size: 14px; line-height: 19px; }
  .read-more {
    display: block; margin: 6px 13px 0; font-size: 12px;
    color: var(--text); text-decoration: none;
  }
  .read-more.is-active { color: var(--accent); }
  .read-more svg { vertical-align: middle; margin-left: 3px; }
  .detail-title {
    position: absolute; left: 73px; top: 402px;
    font-family: "Fjalla One", sans-serif; font-weight: 400; font-size: 27px; line-height: 36px;
    color: var(--heading); text-transform: uppercase;
  }
  .detail-body { position: absolute; left: 74px; top: 450px; width: 1048px; font-size: 16px; line-height: 21.3px; }
  .detail-body p + p { margin-top: 21.3px; }
  .check-list { position: absolute; left: 100px; top: 720px; list-style: none; }
  .check-list li {
    height: 32px; display: flex; align-items: center;
    font-size: 14px; font-weight: 700; font-style: italic;
  }
  .check-list svg { margin-right: 4px; flex: none; }
</style>
</head>
<body>
  <h2 class="section-title">Our Technology</h2>

  <div class="feature-cards">
    <article class="feature-card">
      <h3 class="card-title">Activities</h3>
      <div class="card-media media-care" role="img" aria-label="Photo of a caregiver with an elderly patient"></div>
      <p class="card-text">Lorem ipsum dolor sit amet, consectetur adipiscing elit.</p>
      <a class="read-more is-active" href="#">Read More ····<svg width="6" height="8" viewBox="0 0 6 8"><path d="M1 1l3 3-3 3" fill="none" stroke="currentColor" stroke-width="1.6"/></svg></a>
    </article>
    <article class="feature-card">
      <h3 class="card-title">Assesments</h3>
      <div class="card-media media-assess" role="img" aria-label="Photo of a doctor reviewing a chart with a pen"></div>
      <p class="card-text">Lorem ipsum dolor sit amet, consectetur adipiscing elit.</p>
      <a class="read-more" href="#">Read More ····<svg width="6" height="8" viewBox="0 0 6 8"><path d="M1 1l3 3-3 3" fill="none" stroke="currentColor" stroke-width="1.6"/></svg></a>
    </article>
    <article class="feature-card">
      <h3 class="card-title">How It Works</h3>
      <div class="card-media media-gears" role="img" aria-label="Illustration of green gears"></div>
      <p class="card-text">Lorem ipsum dolor sit amet, consectetur adipiscing elit.</p>
      <a class="read-more" href="#">Read More ····<svg width="6" height="8" viewBox="0 0 6 8"><path d="M1 1l3 3-3 3" fill="none" stroke="currentColor" stroke-width="1.6"/></svg></a>
    </article>
    <article class="feature-card">
      <h3 class="card-title">Clinical Coloboration</h3>
      <div class="card-media media-clinic" role="img" aria-label="Photo of a clinician beside a monitor"></div>
      <p class="card-text">Lorem ipsum dolor sit amet, consectetur adipiscing elit..</p>
      <a class="read-more" href="#">Read More ····<svg width="6" height="8" viewBox="0 0 6 8"><path d="M1 1l3 3-3 3" fill="none" stroke="currentColor" stroke-width="1.6"/></svg></a>
    </article>
  </div>

  <h2 class="detail-title">Activities</h2>
  <div class="detail-body">
    <p>Nulla facilisi. Duis lacinia ultrices faucibus. Maecenas non risus vel sem aliquam iaculis eu sit amet enim. Etiam faucibus mollis dolor sed pulvinar. Ut gravida eros mi, facilisis condimentum mi hendrerit non. Phasellus mattis lacus diam, id lobortis turpis tempor quis. Sed sem justo, ultrices quis ullamcorper non, varius eu diam. Fusce bibendum, diam quis varius elementum, risus ipsum semper nulla, ut laoreet diam arcu a felis. Sed vel nisl tortor. Morbi tincidunt nunc eget interdum tempus. Suspendisse eget ullamcorper libero. Curabitur elementum risus diam, ac egestas nisi porttitor eu. Vivamus quis turpis sed metus sagittis faucibus. Nunc in rutrum sem, a condimentum lorem.</p>
    <p>Cras mollis, augue sit amet luctus consectetur, enim odio placerat ante, ut ultrices est ipsum eget mauris. Nunc eget lacus eu nibh varius fermen-tum. In in semper ante. Cras porttitor leo vitae semper ultrices. Donec consequat elit ac risus varius, ac tempus libero blandit. Donec fringilla nunc sed gravida mattis. In hac habitasse platea dictumst. Quisque euismod scelerisque risus, quis cursus arcu convallis sed. Lorem ipsum dolor sit amet, consectetur adipiscing elit. Nulla cursus ultrices hendrerit. Pellentesque habitant morbi tristique senectus et netus et malesuada fames ac turpis egestas.</p>
  </div>

  <ul class="check-list">
    <li><svg width="34" height="22" viewBox="0 0 34 22"><path d="M1 11l9 9L33 1 10 14z" fill="var(--tick)" stroke="var(--tick-dark)" stroke-width="1"/></svg>Morbi at lorem rutrum, facilisis lacus at, ornare magna.</li>
    <li><svg width="34" height="22" viewBox="0 0 34 22"><path d="M1 11l9 9L33 1 10 14z" fill="var(--tick)" stroke="var(--tick-dark)" stroke-width="1"/></svg>Maecenas in diam malesuada, ornare ligula a, blandit magna.</li>
    <li><svg width="34" height="22" viewBox="0 0 34 22"><path d="M1 11l9 9L33 1 10 14z" fill="var(--tick)" stroke="var(--tick-dark)" stroke-width="1"/></svg>Praesent lobortis libero ac justo volutpat molestie.</li>
    <li><svg width="34" height="22" viewBox="0 0 34 22"><path d="M1 11l9 9L33 1 10 14z" fill="var(--tick)" stroke="var(--tick-dark)" stroke-width="1"/></svg>Mauris a erat rutrum tortor dictum semper eget a velit.</li>
    <li><svg width="34" height="22" viewBox="0 0 34 22"><path d="M1 11l9 9L33 1 10 14z" fill="var(--tick)" stroke="var(--tick-dark)" stroke-width="1"/></svg>Morbi condimentum massa eu scelerisque consequat.</li>
    <li><svg width="34" height="22" viewBox="0 0 34 22"><path d="M1 11l9 9L33 1 10 14z" fill="var(--tick)" stroke="var(--tick-dark)" stroke-width="1"/></svg>Fusce adipiscing enim at mauris tristique vehicula.</li>
  </ul>
</body>
</html>
```